Tandrel needs stationery design

We need desings for presentation cards and letter head for our company. It would be better that the letterhead uses our logo with white background and the presentation card the logo with the black background for the back of the card and the text (name, phone

Colors
0455a3
ec1f27
000000

Requirements
Must have
• Use company logo and colors

```html
<!DOCTYPE html>
<html lang="en">
<head>
<meta charset="utf-8">
<title>Tandrel Stationery</title>
<link href="https://fonts.googleapis.com/css2?family=Montserrat:wght@500&family=Arimo:wght@400&family=Cinzel:wght@400&display=swap" rel="stylesheet">
<style>
  :root {
    --blue: #0455a3;
    --red: #ec1f27;
    --black: #000000;
    --ink: #1b1b1b;
    --paper: #ffffff;
    --grey-text: #5a5a5a;
    --backdrop: #cfcfcf;
  }
  * { box-sizing: border-box; margin: 0; padding: 0; }
  html, body { width: 1200px; height: 768px; overflow: hidden; background: var(--backdrop); }
  .canvas { position: relative; width: 1200px; height: 768px; }

  .wordmark {
    font-family: "Montserrat", sans-serif;
    font-weight: 500;
    letter-spacing: 0.06em;
    display: flex; align-items: center;
  }
  .wordmark .mark-square { display: inline-block; background: var(--red); margin-right: 0.35em; }

  /* Letterhead */
  .letterhead {
    position: absolute; left: 640px; top: 30px; width: 500px; height: 708px;
    background: var(--paper); box-shadow: 0 4px 18px rgba(0,0,0,.18);
    padding: 0 44px;
  }
  .letterhead .top-rule { position: absolute; left: 0; right: 0; top: 0; height: 5px; background: var(--black); }
  .letterhead .wordmark { margin-top: 58px; margin-left: 4px; font-size: 40px; color: var(--ink); }
  .letterhead .wordmark .mark-square { width: 18px; height: 18px; }
  .letter-body {
    margin-top: 52px; font-family: "Arimo", sans-serif; font-size: 9.6px; line-height: 1.5;
    color: var(--grey-text);
  }
  .letter-body p + p { margin-top: 16px; }
  .letter-footer { position: absolute; left: 0; right: 0; bottom: 0; height: 78px; }
  .letter-footer .bands { position: absolute; left: 0; right: 0; top: 0; height: 12px; }
  .letter-footer .band-black { position: absolute; left: 0; top: 6px; height: 3px; width: 72%; background: var(--black); }
  .letter-footer .band-red { position: absolute; left: 30%; top: 0; height: 4px; width: 34%; background: var(--red); }
  .letter-footer .band-red-right { position: absolute; right: 0; top: 0; height: 9px; width: 22%; background: var(--red); }
  .contact-line {
    position: absolute; left: 30px; right: 20px; top: 28px;
    display: flex; justify-content: space-between; align-items: center;
    font-family: "Cinzel", serif; font-size: 8.6px; color: var(--grey-text); letter-spacing: 0.02em;
  }
  .contact-line span { display: flex; align-items: center; gap: 4px; }
  .contact-line svg { width: 9px; height: 9px; fill: var(--red); }
  .letter-footer .bottom-rule { position: absolute; left: 0; right: 0; bottom: 0; height: 6px; background: var(--black); }

  /* Business cards */
  .card { position: absolute; width: 350px; height: 200px; box-shadow: 0 4px 14px rgba(0,0,0,.2); overflow: hidden; }
  .card-back { left: 130px; top: 150px; background: #161515; display: flex; align-items: center; justify-content: center; }
  .card-back .wordmark { font-size: 34px; color: var(--paper); }
  .card-back .wordmark .mark-square { width: 15px; height: 15px; }

  .card-front { left: 200px; top: 400px; background: var(--paper); }
  .card-front .identity { position: absolute; left: 34px; top: 66px; }
  .card-front .wordmark { font-size: 24px; color: var(--ink); }
  .card-front .wordmark .mark-square { width: 10px; height: 10px; }
  .card-front .person { margin-top: 4px; margin-left: 20px; font-family: "Arimo", sans-serif; color: var(--grey-text); }
  .card-front .person .name { font-size: 10px; }
  .card-front .person .role { font-size: 8px; margin-top: 1px; }
  .card-front .divider { position: absolute; left: 196px; top: 40px; width: 1px; height: 82px; background: #c9c9c9; }
  .card-front .details { position: absolute; left: 208px; top: 42px; list-style: none;
    font-family: "Arimo", sans-serif; font-size: 7.5px; line-height: 1.75; color: var(--grey-text); }
  .card-front .details li { display: flex; align-items: center; gap: 5px; }
  .card-front .details li::before { content: ""; width: 4px; height: 4px; border-radius: 50%; background: var(--red); }
  .card-front .band-black { position: absolute; right: 0; top: 150px; width: 46%; height: 10px; background: var(--black); }
  .card-front .band-red { position: absolute; left: 0; bottom: 14px; width: 62%; height: 3px; background: var(--red); }
  .card-front .band-base { position: absolute; left: 0; right: 0; bottom: 0; height: 6px; background: var(--black); }
</style>
</head>
<body>
<main class="canvas">

  <section class="card card-back" aria-label="Business card back">
    <div class="wordmark"><span class="mark-square"></span>TANDREL</div>
  </section>

  <section class="card card-front" aria-label="Business card front">
    <div class="identity">
      <div class="wordmark"><span class="mark-square"></span>TANDREL</div>
      <div class="person">
        <div class="name">Example Name</div>
        <div class="role">Designation</div>
      </div>
    </div>
    <div class="divider"></div>
    <ul class="details">
      <li>0000 Harbor Line Ave,</li>
      <li>Suite 000, Denton, US 0000</li>
      <li>000.000.0047</li>
      <li>contact@tandrel.com</li>
      <li>www.tandrel.com</li>
    </ul>
    <div class="band-black"></div>
    <div class="band-red"></div>
    <div class="band-base"></div>
  </section>

  <article class="letterhead" aria-label="Letterhead">
    <div class="top-rule"></div>
    <div class="wordmark"><span class="mark-square"></span>TANDREL</div>
    <div class="letter-body">
      <p>Lorem Ipsum is simply dummy text of the printing and typesetting industry. Lorem Ipsum has been the industry's standard dummy text ever since the 1500s, when an unknown printer took a galley of type and scrambled it to make a type specimen book. It has survived not only five centuries, but also the leap into electronic typesetting, remaining essentially unchanged. It was popularised in the 1960s with the release of Tessaline sheets containing Lorem Ipsum passages, and more recently with desktop publishing software like Quillset Composer including versions of Lorem Ipsum.</p>
      <p>It is a long established fact that a reader will be distracted by the readable content of a page when looking at its layout. The point of using Lorem Ipsum is that it has a more-or-less normal distribution of letters, as opposed to using 'Content here, content here', making it look like readable English. Many desktop publishing packages and web page editors now use Lorem Ipsum as their default model text, and a search for 'lorem ipsum' will uncover many web sites still in their infancy. Various versions have evolved over the years, sometimes by accident, sometimes on purpose (injected humour and the like).</p>
      <p>Contrary to popular belief, Lorem Ipsum is not simply random text. It has roots in a piece of classical Latin literature from 45 BC, making it over 2000 years old. Doran Pellis, a Latin professor at Marlow Vale College in Oregon, looked up one of the more obscure Latin words, consectetur, from a Lorem Ipsum passage, and going through the cites of the word in classical literature, discovered the undoubtable source. Lorem Ipsum comes from sections 1.10.32 and 1.10.33 of "de Finibus Bonorum et Malorum" structures, to generate Lorem Ipsum which looks reasonable. The generated Lorem Ipsum is therefore always free from repetition, injected humour, or non-characteristic words etc.</p>
    </div>
    <footer class="letter-footer">
      <div class="bands">
        <div class="band-black"></div>
        <div class="band-red"></div>
        <div class="band-red-right"></div>
      </div>
      <div class="contact-line">
        <span><svg viewBox="0 0 10 10" aria-hidden="true"><path d="M5 0a3.4 3.4 0 0 0-3.4 3.4C1.6 6 5 10 5 10s3.4-4 3.4-6.6A3.4 3.4 0 0 0 5 0zm0 4.8a1.4 1.4 0 1 1 0-2.8 1.4 1.4 0 0 1 0 2.8z"/></svg>0000 Harbor Line Ave, Suite 000, Denton, US 0000</span>
        <span><svg viewBox="0 0 10 10" aria-hidden="true"><path d="M2 0.5l2 2-1 1.3a6 6 0 0 0 3.2 3.2l1.3-1 2 2-1.2 1.5C4.5 9.5 0.5 5.5 0.5 1.7z"/></svg>000.000.0047</span>
        <span><svg viewBox="0 0 10 10" aria-hidden="true"><path d="M0 2h10v6H0zM0.8 2.6 5 5.6l4.2-3H0.8z"/></svg>contact@tandrel.com</span>
        <span><svg viewBox="0 0 10 10" aria-hidden="true"><circle cx="5" cy="5" r="4.6"/></svg>www.tandrel.com</span>
      </div>
      <div class="bottom-rule"></div>
    </footer>
  </article>

</main>
</body>
</html>
```